Judicial Invitation for Political Campaign

I need an invitation template for a judicial fundraiser for political candidtate in Texas.  The invitation will be a flat size of 10 x 7 and a folded size of 5 x 7.  Can fold horizontal or vertical.  Invitation must incorporate the candidate's logo in the design.
I have multiple candidates so this could be an on-going project.  I have attached the various candidate logos so you may choose and work with whatever logo you prefer...
the inside panels of the invitation will have various text added as the events get finalized so right now I just need any design that you would like to add to the inside.  It should be light enough or framed so that there is sufficient room at the top or right side for a large list of contributors and the bottom or left side will have information about the event.
Please feel free to email if you need clarification.

Updates
Logos have been uploaded.  Please use only one logo per invitation.  Each candidate will have separate events.

Industry/Entity Type
Political
Look and feel

```html
<!DOCTYPE html>
<html lang="en">
<head>
<meta charset="utf-8">
<title>Judicial Fundraiser Invitation</title>
<link rel="stylesheet" href="https://fonts.googleapis.com/css2?family=Metamorphous&family=Josefin+Sans:wght@300;400&family=Montserrat:wght@800&family=Open+Sans:wght@800&family=Ubuntu:wght@300&display=swap">
<style>
  :root {
    --cover-light: #ffe08a;
    --cover-mid: #fbb63c;
    --cover-deep: #f0871c;
    --ink: #1a1410;
    --claret: #8e1a10;
    --claret-bright: #a3180f;
    --script-gold: #fff0b8;
    --parchment: #f3e2c2;
    --parchment-edge: #d5b486;
    --parchment-band: #e3c9a0;
    --muted-brown: #9b7c5c;
    --list-ink: #5b4a3a;
    --frame-fill: #c3ae8b;
    --paper-white: #ffffff;
    --bronze-light: #e39a48;
    --bronze-mid: #b8662a;
    --bronze-deep: #7c3f18;
    --dash: rgba(120, 70, 20, 0.55);
  }
  * { margin: 0; padding: 0; box-sizing: border-box; }
  html, body { width: 1200px; height: 840px; overflow: hidden; background: #fff; }
  .invitation { position: relative; width: 1200px; height: 840px; overflow: hidden; }

  .cover {
    position: absolute; left: 0; top: 0; width: 600px; height: 840px;
    background: linear-gradient(180deg, var(--cover-deep) 0%, var(--cover-mid) 35%, var(--cover-light) 75%, #fff3d0 100%);
  }
  .cover__rule {
    position: absolute; left: 54px; width: 500px; border-top: 2px dashed var(--dash);
  }
  .cover__centered {
    position: absolute; left: 10px; width: 600px; text-align: center;
  }
  .cover__script {
    top: 42px;
    font-family: "Metamorphous", serif; font-size: 60px; line-height: 1.1; color: var(--script-gold);
    text-shadow: 0 0 1px #b86a10;
  }
  .cover__title {
    font-family: "Josefin Sans", sans-serif; font-weight: 300; line-height: 1;
  }
  .cover__title--judicial { top: 124px; font-size: 76px; color: var(--ink); }
  .cover__title--fundraiser { top: 184px; font-size: 54px; color: var(--claret); padding-left: 62px; }
  .cover__title--fundraiser .for { font-size: 28px; color: var(--ink); font-weight: 400; }
  .cover__candidate {
    top: 226px;
    font-family: "Montserrat", sans-serif; font-weight: 800; font-size: 33px; color: var(--ink);
  }
  .cover__state {
    position: absolute; left: 246px; top: 274px; width: 114px; height: 27px;
    background: var(--claret); color: #fff; text-align: center;
    font-family: "Josefin Sans", sans-serif; font-weight: 400; font-size: 18px; line-height: 29px;
  }
  .cover__events {
    top: 338px;
    font-family: "Josefin Sans", sans-serif; font-weight: 300; font-size: 24px; color: var(--ink);
  }
  .cover__photo {
    position: absolute; left: 170px; top: 470px; width: 430px; height: 320px;
    border-radius: 180px 0 0 0;
    background: linear-gradient(160deg, var(--bronze-light) 0%, var(--bronze-mid) 50%, var(--bronze-deep) 100%);
  }

  .inside {
    position: absolute; left: 600px; top: 0; width: 600px; height: 840px;
    background: radial-gradient(ellipse 70% 60% at 50% 40%, var(--parchment), var(--parchment-edge));
  }
  .inside__band { position: absolute; left: 0; top: 0; width: 600px; height: 840px; }
  .inside__kicker {
    position: absolute; left: -16px; width: 600px; top: 68px; text-align: center;
    font-family: "Josefin Sans", sans-serif; font-weight: 300; font-size: 38px; color: var(--muted-brown);
  }
  .inside__heading {
    position: absolute; left: -16px; width: 600px; top: 102px; text-align: center;
    font-family: "Open Sans", sans-serif; font-weight: 800; font-size: 48px; color: var(--claret-bright);
  }
  .contributor-list {
    position: absolute; left: 60px; top: 170px; width: 490px;
    display: grid; grid-template-columns: repeat(3, 161px);
    list-style: none;
    font-family: "Ubuntu", sans-serif; font-weight: 300; font-size: 24px; color: var(--list-ink);
  }
  .contributor-list li { height: 34.3px; line-height: 34.3px; }
  .photo-frame {
    position: absolute; width: 150px; height: 150px;
    background: var(--frame-fill); border: 6px solid var(--paper-white);
    box-shadow: 0 1px 3px rgba(90, 60, 30, 0.25);
  }

  .fold-wave { position: absolute; left: 0; top: 0; width: 1200px; height: 840px; }
</style>
</head>
<body>
<main class="invitation">
  <section class="cover">
    <div class="cover__rule" style="top:46px"></div>
    <div class="cover__centered cover__script">Invitation</div>
    <div class="cover__rule" style="top:114px"></div>
    <div class="cover__centered cover__title cover__title--judicial">JUDICIAL</div>
    <div class="cover__centered cover__title cover__title--fundraiser">FUNDRAISER <span class="for">FOR</span></div>
    <div class="cover__centered cover__candidate">POLITICAL CANDIDTATE</div>
    <div class="cover__state">IN TEXAS</div>
    <div class="cover__rule" style="top:330px"></div>
    <div class="cover__centered cover__events">EVENTS</div>
    <div class="cover__rule" style="top:372px"></div>
    <div class="cover__photo" role="img" aria-label="Photograph of a bronze judge's gavel"></div>
  </section>

  <section class="inside">
    <svg class="inside__band" viewBox="0 0 600 840" aria-hidden="true">
      <path d="M0,700 C80,640 200,650 300,690 C420,740 520,680 600,660 L600,840 L0,840 Z" fill="var(--parchment-band)"/>
    </svg>
    <div class="inside__kicker">LIST OF</div>
    <h1 class="inside__heading">CONTRIBUTORS</h1>
    <ul class="contributor-list">
      <li>contributors</li><li>contributors</li><li>contributors</li>
      <li>contributors</li><li>contributors</li><li>contributors</li>
      <li>contributors</li><li>contributors</li><li>contributors</li>
      <li>contributors</li><li>contributors</li><li>contributors</li>
      <li>contributors</li><li>contributors</li><li>contributors</li>
      <li>contributors</li><li>contributors</li><li>contributors</li>
      <li>contributors</li><li>contributors</li><li>contributors</li>
      <li>contributors</li><li>contributors</li><li>contributors</li>
    </ul>
    <div class="photo-frame" style="left:58px;top:537px;transform:rotate(-10deg)"></div>
    <div class="photo-frame" style="left:223px;top:487px;transform:rotate(4deg)"></div>
    <div class="photo-frame" style="left:395px;top:472px;transform:rotate(-4deg)"></div>
    <div class="photo-frame" style="left:157px;top:615px;transform:rotate(4deg)"></div>
    <div class="photo-frame" style="left:463px;top:569px;transform:rotate(-5deg)"></div>
  </section>

  <svg class="fold-wave" viewBox="0 0 1200 840" aria-hidden="true">
    <path d="M0,748 C120,735 260,750 380,775 C430,786 470,790 500,788 C560,784 600,760 600,760 L600,840 L0,840 Z" fill="var(--paper-white)" opacity="0.92"/>
    <path d="M600,760 C640,740 680,790 720,800 C820,820 900,790 1000,760 C1080,736 1150,725 1200,720 L1200,840 L600,840 Z" fill="var(--paper-white)"/>
  </svg>
</main>
</body>
</html>
```